Korvane Design Template

I'd like to have a powerpoint templates. In particular a resume template design upon the Korvane website (www.korvane.nl). Korvane is the overarching label in grey tones. The website is therefore more focussed on Techkorvane in blue colors, I expect more korvanes in the future with different color tones.

The resume template can hopefulle reused as template for business development and more.

The template should be highly professional. Preferably with a one-pager summary in front and 2 work experience details and last page with education/certificates and competences.

The onepager master slide should include
- Profile picture
- Name
- About me (optionally to mention this literally, this text can be alongside/next to the profile picture
- Table of work experience summary

In short, age, place of living, mobile phone nr in footer?
In the workexperience it describes Role, timeframe, subtitle used in slide 1 (summary of role), with a section of scope and section for achievements.

From a visual perspective, please stick to the logos provided. You may want to grey out the logo. Keep the logo as it is and work with collor pallet
Light Grey: #DEDEDE
Medium Grey: #888888
Black: #3A3A3A

```html
<!DOCTYPE html>
<html lang="en">
<head>
<meta charset="utf-8">
<title>Korvane Resume Template</title>
<link rel="stylesheet" href="https://fonts.googleapis.com/css2?family=Roboto:wght@400;500;700&display=swap">
<style>
:root{
  --stage:#979797;
  --light-grey:#DEDEDE;
  --panel:#EFEFEF;
  --medium-grey:#888888;
  --ink:#3A3A3A;
  --paper:#FFFFFF;
}
*{box-sizing:border-box;margin:0;padding:0}
html,body{width:1200px;height:820px;overflow:hidden}
body{background:var(--stage);font-family:'Roboto',Arial,sans-serif;color:var(--ink);position:relative}
.resume{position:absolute;top:35px;width:519px;height:733px;background:linear-gradient(180deg,var(--paper) 0%,var(--paper) 68%,#ECECEC 100%);overflow:hidden}
.resume--first{left:54px}
.resume--second{left:623px}
.sidebar{position:absolute;left:11px;top:9px;width:191px;height:724px;background:linear-gradient(180deg,var(--light-grey) 0%,var(--light-grey) 70%,#E6E6E6 100%)}
.header-panel{position:absolute;left:100px;top:31px;width:398px;height:160px;border-radius:18px;background:var(--panel)}
.portrait-ring{position:absolute;left:31px;top:31px;width:162px;height:162px;border-radius:50%;background:var(--paper)}
.portrait{position:absolute;left:38px;top:38px;width:148px;height:148px;border-radius:50%;background:radial-gradient(circle at 50% 45%,#8d7f78 0%,#5d5b66 38%,#cfd7e8 60%,#d9e0ee 100%)}
.name{position:absolute;left:223px;top:47px;font-size:23px;font-weight:700;letter-spacing:.3px;white-space:nowrap}
.role-title{position:absolute;left:223px;top:74px;font-size:13px;white-space:nowrap}
.dash{position:absolute;top:98px;height:3px;border-radius:2px;background:var(--medium-grey)}
.dash--short{left:225px;width:16px}
.dash--long{left:244px;width:34px}
.about{position:absolute;left:224px;top:114px;width:262px;font-size:6.6px;line-height:11px;text-align:justify}
.wordmark{position:absolute;left:38px;top:199px;font-size:34px;font-weight:400;letter-spacing:.5px;line-height:1}
.wordmark-shadow{position:absolute;left:50px;top:242px;width:120px;height:5px;border-radius:50%;background:radial-gradient(ellipse,rgba(0,0,0,.12),rgba(0,0,0,0) 70%)}
.section-head{position:absolute;display:flex;align-items:center;gap:5px;font-size:13.5px;font-weight:700;white-space:nowrap}
.section-head svg{width:13px;height:13px;fill:var(--ink)}
.edu{position:absolute;left:43px;width:148px}
.edu-school{font-size:7.8px;line-height:10.5px;position:relative;padding-left:10px}
.edu-school::before,.edu-degree::before{content:"";position:absolute;left:0;top:4px;width:2.5px;height:2.5px;border-radius:50%;background:var(--ink)}
.edu-degree{font-size:5.8px;line-height:8px;position:relative;padding-left:10px;margin-top:4px}
.edu-years{font-size:6.8px;margin-top:7px;padding-left:10px}
.edu--plain .edu-degree{padding-left:0}
.edu--plain .edu-degree::before{display:none}
.edu--plain .edu-years{padding-left:0}
.skills{position:absolute;left:38px;width:150px;list-style:none}
.skills li{position:relative;padding-left:9px;font-size:8px;line-height:12.4px}
.skills li::before{content:"";position:absolute;left:0;top:5px;width:2.5px;height:2.5px;border-radius:50%;background:var(--ink)}
.contact-row{position:absolute;left:38px;display:flex;align-items:center;font-size:8px;white-space:nowrap;height:14px}
.contact-row svg{width:10px;height:10px;fill:var(--ink)}
.contact-row .divider{width:1px;height:13px;background:var(--ink);margin:0 9px 0 8px}
.footer-site{position:absolute;left:35px;top:713px;font-size:7.8px}
.footer-rule{position:absolute;left:93px;top:718px;width:392px;height:1px;background:var(--medium-grey)}
.exp-head{left:229px;top:200px}
.exp-rule{position:absolute;left:338px;top:208px;width:147px;height:1px;background:var(--ink)}
.dot{position:absolute;left:227px;width:8px;height:8px;border-radius:50%;background:var(--ink)}
.stem{position:absolute;left:230.5px;width:1px;height:12px;background:var(--ink)}
.rail{position:absolute;left:230.5px;width:1px;background:var(--ink)}
.org{position:absolute;left:242px;font-size:7.6px;font-weight:700;white-space:nowrap}
.post{position:absolute;left:242px;font-size:6.8px;color:var(--medium-grey);white-space:nowrap}
.when{position:absolute;right:34px;font-size:6.8px;color:var(--medium-grey);white-space:nowrap;text-align:right}
.role{position:absolute;left:251px;font-size:7.6px;color:var(--medium-grey);white-space:nowrap}
.role::before{content:"";position:absolute;left:-12px;top:4px;width:8px;height:1px;background:var(--medium-grey)}
.role::after{content:"";position:absolute;left:-7px;top:2.5px;width:4px;height:4px;border-radius:50%;background:var(--medium-grey)}
.desc{position:absolute;left:242px;width:243px;font-size:6.8px;line-height:9.4px;text-align:justify}
.desc--wide{left:224px;width:261px;text-align:left}
</style>
</head>
<body>

<section class="resume resume--first" aria-label="Resume Joris Vermeulen">
  <div class="sidebar"></div>
  <div class="header-panel"></div>
  <div class="portrait-ring"></div>
  <div class="portrait" role="img" aria-label="Profile photo of Joris Vermeulen"></div>
  <h1 class="name">JORIS VERMEULEN</h1>
  <p class="role-title">Korvane Lead | Director IT</p>
  <span class="dash dash--short"></span><span class="dash dash--long"></span>
  <p class="about">Experienced Technology Director with a demonstrated history of working in the retail industry. Experienced leader in DevOps, Architecture, Program Delivery and Service Delivery positions. Extensive experience in working conform PMP, PRINCE2, SAFE, Agile/ Scrum, ITIL, DevOps in areas of Network, Cloud, Integration, API, Automation, Workplace Services exceeding 50Mio annual budget.</p>

  <div class="wordmark">korvane</div>
  <div class="wordmark-shadow"></div>

  <h2 class="section-head" style="left:35px;top:252px"><svg viewBox="0 0 16 16"><circle cx="8" cy="3" r="2.5"/><path d="M4 7h8l-2 4H6z"/><path d="M1 9c2 3 4 5 7 6 3-1 5-3 7-6-3 1-5 2-7 4-2-2-4-3-7-4z"/></svg>EDUCATION</h2>
  <div class="edu" style="top:278px">
    <p class="edu-school">Eemland University of Applied Sciences Amersfoort (Hogeschool Eemland)</p>
    <p class="edu-degree">Bachelor of Business Administration - BBA Business Administration, Management and Operations</p>
    <p class="edu-years">2005 - 2008</p>
  </div>

  <h2 class="section-head" style="left:35px;top:342px"><svg viewBox="0 0 16 16"><path d="M8 2a4.5 4.5 0 0 0-2.5 8.2V12h5v-1.8A4.5 4.5 0 0 0 8 2z"/><rect x="5.5" y="13" width="5" height="1.5"/><path d="M1 6h2M13 6h2M3 1.5l1.3 1.3M13 1.5l-1.3 1.3" stroke="#3A3A3A" stroke-width="1"/></svg>SKILLS</h2>
  <ul class="skills" style="top:367px">
    <li>Retail</li><li>Enterprise Software</li><li>Business Analysis</li><li>Service Delivery</li><li>PRINCE2</li><li>IT Service Management</li><li>ICT</li><li>ITIL</li><li>Outsourcing</li><li>Management</li><li>Change Management</li><li>Incident Management</li><li>Service Management</li><li>IT Management</li><li>Governance</li>
  </ul>

  <h2 class="section-head" style="left:36px;top:564px"><svg viewBox="0 0 16 16"><rect x="3" y="1" width="11" height="14" rx="1"/><rect x="1" y="3" width="3" height="1.5"/><rect x="1" y="7" width="3" height="1.5"/><rect x="1" y="11" width="3" height="1.5"/><circle cx="9" cy="6" r="2" fill="#DEDEDE"/><path d="M5.5 12c0-2 1.5-3 3.5-3s3.5 1 3.5 3z" fill="#DEDEDE"/></svg>CONTACT</h2>
  <div class="contact-row" style="top:592px"><svg viewBox="0 0 16 16"><path d="M4 0h8a1 1 0 0 1 1 1v14a1 1 0 0 1-1 1H4a1 1 0 0 1-1-1V1a1 1 0 0 1 1-1zm1 2v10h6V2z"/></svg><span class="divider"></span>+123-456-7890</div>
  <div class="contact-row" style="top:614px"><svg viewBox="0 0 16 16"><path d="M0 3h16v10H0z"/><path d="M0 3l8 6 8-6" fill="none" stroke="#DEDEDE" stroke-width="1.2"/></svg><span class="divider"></span>joris.vermeulen@korvane.nl</div>
  <div class="contact-row" style="top:633px"><svg viewBox="0 0 16 16"><path d="M3 1l10 6-4 1.2 3 5.3-2 1.1-3-5.3L4 12z"/></svg><span class="divider"></span>www.vontel.pro</div>
  <div class="contact-row" style="top:653px"><svg viewBox="0 0 16 16"><path d="M8 0a5.5 5.5 0 0 0-5.5 5.5C2.5 10 8 16 8 16s5.5-6 5.5-10.5A5.5 5.5 0 0 0 8 0zm0 8a2.5 2.5 0 1 1 0-5 2.5 2.5 0 0 1 0 5z"/></svg><span class="divider"></span>The Lowmark, Veldland</div>
  <div class="contact-row" style="top:675px"><svg viewBox="0 0 16 16"><circle cx="8" cy="8" r="7.5"/></svg><span class="divider"></span>Joris Vermeulen</div>

  <h2 class="section-head exp-head"><svg viewBox="0 0 16 16"><circle cx="6" cy="4" r="2.5"/><path d="M1 14c0-4 2-6 5-6s5 2 5 6z"/><circle cx="12.5" cy="12.5" r="2.5" fill="none" stroke="#3A3A3A" stroke-width="1.2"/></svg>EXPERIENCE</h2>
  <span class="exp-rule"></span>

  <span class="dot" style="top:231px"></span><span class="stem" style="top:238px"></span>
  <p class="org" style="top:229px">Korvane</p>
  <p class="post" style="top:241px">Korvane Lead</p><p class="when" style="top:241px">Jun 2025 - Present</p>
  <p class="desc desc--wide" style="top:255px">Korvane Lead and Partner; serving the community of engineering teams.</p>

  <span class="dot" style="top:272px"></span><span class="stem" style="top:279px"></span>
  <p class="org" style="top:270px">Lindemaar University</p>
  <p class="post" style="top:282px">Department Manager IT Infrastructure (a.i.)</p><p class="when" style="top:282px">May 2023 - Present</p>

  <span class="dot" style="top:303px"></span><span class="stem" style="top:310px"></span>
  <p class="org" style="top:301px">KESTRAKESTRA</p>
  <p class="post" style="top:312px">COO KESTRA</p><p class="when" style="top:312px">Oct 2023 - Jul 2025</p>

  <span class="dot" style="top:331px"></span><span class="stem" style="top:338px"></span>
  <p class="org" style="top:329px">Partner VONTEL</p>
  <p class="post" style="top:341px">VONTELVONTEL</p><p class="when" style="top:341px">Feb 2021 - Jul 2025</p>

  <span class="dot" style="top:364px"></span><span class="rail" style="top:370px;height:80px"></span>
  <p class="org" style="top:362px">Marktveld</p><p class="when" style="top:362px">5 yrs 2 mos</p>
  <p class="role" style="top:377px">Director Technology</p><p class="when" style="top:377px">Oct 2017 to Feb 2021</p>
  <p class="desc" style="top:392px">Development &amp; Operations for Network, Hosting (On Prem and Cloud), Integration, Automation and Workplace Services</p>
  <p class="role" style="top:419px">Program Manager Technology</p><p class="when" style="top:419px">Jan 2016 - Oct 2017</p>
  <p class="desc" style="top:434px">Program Manager for the Technology Portfolio. Initiatives covering network, datacenter, security, store and integration improvements</p>

  <span class="dot" style="top:462px"></span><span class="rail" style="top:468px;height:83px"></span>
  <p class="org" style="top:460px">Marktveld Groep</p><p class="when" style="top:460px">4 yrs 1 mos</p>
  <p class="role" style="top:475px">Domain Infrastructure Architect - Technology</p><p class="when" style="top:475px">Jan 2014 - Jan 2016</p>
  <p class="desc" style="top:491px;text-align:left">Led infrastructure strategy, demand forecasting, and portfolio planning across IT domains. Appointed Program Manager for tech projects (a.i.) in late 2015.</p>
  <p class="role" style="top:518px">Enterprise Architect and Service Delivery Manager</p><p class="when" style="top:518px">Jan 2012 - 2014</p>
  <p class="desc" style="top:533px">Held dual role as Enterprise Architect and Service Delivery Manager for network, telephony, collaboration, EUC, and IAM.</p>

  <span class="dot" style="top:563px"></span><span class="rail" style="top:569px;height:127px"></span>
  <p class="org" style="top:561px">Marktveld</p><p class="when" style="top:561px">9 yrs 11 mos</p>
  <p class="role" style="top:575px">Project Manager</p><p class="when" style="top:575px">Sep 2009 - Apr 2011</p>
  <p class="desc" style="top:589px">Cloud Suite Implementation Lead</p>
  <p class="role" style="top:603px">IT Trainee / IT Enterprise Planning</p><p class="when" style="top:603px">Sep 2008 - Sep 2009</p>
  <p class="desc" style="top:618px">Operating model improvements, small changes, collaboration platform rationalization.</p>
  <p class="role" style="top:647px">Parttime Teamlead</p><p class="when" style="top:647px">Jan 2006 - Sep 2008</p>
  <p class="desc" style="top:660px">Operational responsible for warehouse operation national fresh centre</p>
  <p class="role" style="top:675px">Parttime Operations &amp; Logistics Analyst</p><p class="when" style="top:675px">Jun 2001 - Jan 2006</p>
  <p class="desc" style="top:688px">Optimization / analytics of warehouse operations</p>

  <p class="footer-site">www.korvane.nl</p><span class="footer-rule"></span>
</section>

<section class="resume resume--second" aria-label="Resume Sander Holt">
  <div class="sidebar"></div>
  <div class="header-panel"></div>
  <div class="portrait-ring"></div>
  <div class="portrait" role="img" aria-label="Profile photo of Sander Holt" style="background:radial-gradient(circle at 50% 42%,#c79a82 0%,#a8755a 35%,#cdd6e8 62%,#d9e0ee 100%)"></div>
  <h1 class="name">SANDER HOLT</h1>
  <p class="role-title">Korvane Lead | IT Specialist Cloud</p>
  <span class="dash dash--short"></span><span class="dash dash--long"></span>
  <p class="about">Lorem Ipsum is simply dummy text of the printing and typesetting industry. Lorem Ipsum has been the industry's standard dummy text ever since the 1500s, when an unknown printer took a galley of type and scrambled it to make a type specimen book. It has survived not only five centuries, but also the leap into electronic typesetting, remaining essentially unchanged.</p>

  <div class="wordmark">korvane</div>
  <div class="wordmark-shadow"></div>

  <h2 class="section-head" style="left:35px;top:252px"><svg viewBox="0 0 16 16"><circle cx="8" cy="3" r="2.5"/><path d="M4 7h8l-2 4H6z"/><path d="M1 9c2 3 4 5 7 6 3-1 5-3 7-6-3 1-5 2-7 4-2-2-4-3-7-4z"/></svg>EDUCATION</h2>
  <div class="edu edu--plain" style="top:278px">
    <p class="edu-school" style="margin-left:5px">University of Noorderveen</p>
    <p class="edu-degree">Bachelor of Arts (BA), GeschiedenisBachelor of Arts (BA), Geschiedenis</p>
    <p class="edu-years">2008 - 2011</p>
    <p class="edu-school" style="margin-left:5px;margin-top:8px">University of Noorderveen</p>
    <p class="edu-degree">Master of Arts (MA), Geschiedenis</p>
    <p class="edu-years" style="margin-top:5px">20011 - 2015</p>
  </div>

  <h2 class="section-head" style="left:35px;top:387px"><svg viewBox="0 0 16 16"><path d="M8 2a4.5 4.5 0 0 0-2.5 8.2V12h5v-1.8A4.5 4.5 0 0 0 8 2z"/><rect x="5.5" y="13" width="5" height="1.5"/><path d="M1 6h2M13 6h2M3 1.5l1.3 1.3M13 1.5l-1.3 1.3" stroke="#3A3A3A" stroke-width="1"/></svg>SKILLS</h2>
  <ul class="skills" style="top:411px;width:112px">
    <li>Cloud Architecture &amp; Engineering</li><li>Infrastructure as Code (IaC)</li><li>Security &amp; Compliance</li><li>DevOps &amp; CI/CD</li><li>IT Service Management</li><li>Scripting &amp; Automation</li><li>Monitoring &amp; Performance Management</li>
  </ul>

  <h2 class="section-head" style="left:36px;top:561px"><svg viewBox="0 0 16 16"><rect x="3" y="1" width="11" height="14" rx="1"/><rect x="1" y="3" width="3" height="1.5"/><rect x="1" y="7" width="3" height="1.5"/><rect x="1" y="11" width="3" height="1.5"/><circle cx="9" cy="6" r="2" fill="#DEDEDE"/><path d="M5.5 12c0-2 1.5-3 3.5-3s3.5 1 3.5 3z" fill="#DEDEDE"/></svg>CONTACT</h2>
  <div class="contact-row" style="top:589px"><svg viewBox="0 0 16 16"><path d="M4 0h8a1 1 0 0 1 1 1v14a1 1 0 0 1-1 1H4a1 1 0 0 1-1-1V1a1 1 0 0 1 1-1zm1 2v10h6V2z"/></svg><span class="divider"></span>+123-456-7890</div>
  <div class="contact-row" style="top:611px"><svg viewBox="0 0 16 16"><path d="M0 3h16v10H0z"/><path d="M0 3l8 6 8-6" fill="none" stroke="#DEDEDE" stroke-width="1.2"/></svg><span class="divider"></span>sander.holt@korvane.nl</div>
  <div class="contact-row" style="top:630px"><svg viewBox="0 0 16 16"><path d="M3 1l10 6-4 1.2 3 5.3-2 1.1-3-5.3L4 12z"/></svg><span class="divider"></span>www.website.com</div>
  <div class="contact-row" style="top:651px"><svg viewBox="0 0 16 16"><path d="M8 0a5.5 5.5 0 0 0-5.5 5.5C2.5 10 8 16 8 16s5.5-6 5.5-10.5A5.5 5.5 0 0 0 8 0zm0 8a2.5 2.5 0 1 1 0-5 2.5 2.5 0 0 1 0 5z"/></svg><span class="divider"></span>Dorrevaart, West Holmland, Veldland</div>
  <div class="contact-row" style="top:672px"><svg viewBox="0 0 16 16"><circle cx="8" cy="8" r="7.5"/></svg><span class="divider"></span>Sander Holt</div>

  <h2 class="section-head exp-head"><svg viewBox="0 0 16 16"><circle cx="6" cy="4" r="2.5"/><path d="M1 14c0-4 2-6 5-6s5 2 5 6z"/><circle cx="12.5" cy="12.5" r="2.5" fill="none" stroke="#3A3A3A" stroke-width="1.2"/></svg>EXPERIENCE</h2>
  <span class="exp-rule"></span>

  <span class="dot" style="top:231px"></span><span class="stem" style="top:238px"></span>
  <p class="org" style="top:229px">Korvane</p>
  <p class="post" style="top:241px">Korvane Lead</p><p class="when" style="top:241px">Jun 2025 - Present</p>
  <p class="desc desc--wide" style="top:252px">Korvane Lead and Partner - serving the community of engineering teams.</p>

  <span class="dot" style="top:270px"></span><span class="stem" style="top:277px"></span>
  <p class="org" style="top:268px">Universiteit Zuidermaar</p>
  <p class="post" style="top:279px">Platform Architect Cloud</p><p class="when" style="top:279px">Jan 2025 - Present</p>

  <span class="dot" style="top:298px"></span><span class="stem" style="top:305px"></span>
  <p class="org" style="top:296px">Universiteit Lindemaar</p>
  <p class="post" style="top:307px">Platform Architect Cloud &amp; Product Owner</p><p class="when" style="top:307px">Sep 2023 - Present</p>

  <span class="dot" style="top:328px"></span><span class="stem" style="top:335px"></span>
  <p class="org" style="top:326px">KESTRA</p>
  <p class="post" style="top:337px">Cloud Lead</p><p class="when" style="top:337px">Oct 2023 - Jul 2025</p>

  <span class="dot" style="top:359px"></span><span class="stem" style="top:366px"></span>
  <p class="org" style="top:357px">VONTEL</p>
  <p class="post" style="top:368px">Cloud Lead &amp; Trainer</p><p class="when" style="top:367px">Nov 2021 - Nov 2023</p>

  <span class="dot" style="top:386px"></span><span class="stem" style="top:393px"></span>
  <p class="org" style="top:384px">KP</p>
  <p class="post" style="top:395px">Senior Project manager Cloud Migratie</p><p class="when" style="top:395px">Nov 2022 - Sep 2023</p>

  <span class="dot" style="top:414px"></span><span class="stem" style="top:421px"></span>
  <p class="org" style="top:412px">Telvo</p>
  <p class="post" style="top:423px">MasterClass Professional bij Telvo</p><p class="when" style="top:423px">Apr 2017 - Jul 2019</p>

  <span class="dot" style="top:441px"></span><span class="stem" style="top:448px;height:16px"></span>
  <p class="org" style="top:439px">Leeshuis</p>
  <p class="post" style="top:450px;white-space:normal;width:130px;line-height:9.4px">Boekhandel van den BergBoekhandel van den Berg</p><p class="when" style="top:450px">Oct 2014 - Mar 2017</p>

  <p class="footer-site">www.korvane.nl</p><span class="footer-rule"></span>
</section>

</body>
</html>
```